Paraffin Wax Packaging Design for Nail and Beauty Industry

We need an attractive design for the packaging of our new product, Paraffin Wax. Our company is a wholesale beauty/nail supply company that has been selling to nail salons in the US market for 10 years. We currently sell this product that we buy from another company. Now we want to launch our own brand of Paraffin Wax.

Target Market(s)

Retail nail salons in the US market.

Industry/Entity Type

Industry

Font styles to use
Sans Serif

Colors

Designer to choose colors to be used in the design.

Requirements
Must have
• Our logo (attached).
• All information on the "Ingredient List" (attached).
• Design for Clear Packaging so product can show through.
• Design for Package Dimensions of 4.25" x 11" (110cm x 280 cm).
Nice to have
• Picture related to women's skin and or beauty.
• Contrast as in the design of product that we currently sell (attached).

```html
<!DOCTYPE html>
<html lang="en">
<head>
<meta charset="utf-8">
<title>Premium Paraffin Wax – Package Front</title>
<link href="https://fonts.googleapis.com/css2?family=Montserrat:wght@800&family=Libre+Baskerville:wght@700&family=Tinos:wght@400;700&family=Poppins:wght@400&display=swap" rel="stylesheet">
<style>
  :root {
    --canvas-bg: #f2f2f4;
    --pack-bg: #ffffff;
    --band-purple: #433a8c;
    --ring-black: #2b2b2d;
    --ink: #1c1c1c;
    --white: #ffffff;
    --photo-light: #f3ece6;
    --photo-skin: #dcae90;
  }
  * { margin: 0; padding: 0; box-sizing: border-box; }
  html, body {
    width: 1120px; height: 1200px; overflow: hidden;
    background: var(--canvas-bg);
  }
  .package {
    position: absolute; left: 335px; top: 20px;
    width: 450px; height: 1160px;
    background: var(--pack-bg);
    overflow: hidden;
  }
  .shape-layer { position: absolute; left: 0; top: 0; }
  .brand-name {
    position: absolute; left: 0; right: 0; top: 80px;
    text-align: center;
    font-family: "Montserrat", sans-serif; font-weight: 800;
    font-size: 44px; color: var(--white); letter-spacing: 1px;
  }
  .product-title {
    position: absolute; left: 0; right: 0; top: 203px;
    text-align: center;
    font-family: "Montserrat", sans-serif; font-weight: 800;
    color: var(--white); line-height: 53px; font-size: 46px;
  }
  .claims {
    position: absolute; right: 45px; top: 400px; text-align: right;
    font-family: "Libre Baskerville", serif; font-weight: 700; color: var(--ink);
  }
  .claims .compat { font-size: 25px; line-height: 34px; }
  .claims .benefit { font-size: 18.5px; line-height: 27px; margin-top: 8px; }
  .hero-photo {
    position: absolute; left: 12px; top: 600px; width: 436px; height: 335px;
    background: radial-gradient(ellipse 60% 55% at 45% 62%, var(--photo-skin) 0%, var(--photo-light) 65%, rgba(255,255,255,0) 100%);
  }
  .label-info {
    position: absolute; left: 0; right: 0; top: 1003px; text-align: center; color: var(--ink);
  }
  .ingredients-title { font-family: "Tinos", serif; font-weight: 700; font-size: 15.5px; line-height: 20px; }
  .ingredients-list { font-family: "Tinos", serif; font-size: 14px; line-height: 20px; }
  .caution-title, .caution-text { font-family: "Poppins", sans-serif; font-size: 12.5px; line-height: 16px; }
  .caution-title { margin-top: 4px; }
  .net-weight { font-family: "Poppins", sans-serif; font-size: 16px; margin-top: 10px; }
</style>
</head>
<body>
  <main class="package">
    <svg class="shape-layer" width="450" height="1160" viewBox="0 0 450 1160">
      <path d="M0 0 H450 V472 H0 Z" fill="var(--band-purple)"/>
      <circle cx="282" cy="540" r="185" fill="var(--white)"/>
    </svg>

    <div class="hero-photo" role="img" aria-label="Photo of a woman in a white top seated with bare legs, resting her chin on her hand"></div>

    <svg class="shape-layer" width="450" height="1160" viewBox="0 0 450 1160">
      <path fill="var(--ring-black)" fill-rule="evenodd"
        d="M63 531 a205 205 0 1 0 410 0 a205 205 0 1 0 -410 0 Z
           M97 540 a185 185 0 1 0 370 0 a185 185 0 1 0 -370 0 Z"/>
    </svg>

    <div class="brand-name">By Marisol</div>

    <h1 class="product-title">PREMIUM<br>PARAFFIN WAX</h1>

    <div class="claims">
      <p class="compat">Compatible for<br>use with most<br>wax paraffin heat<br>therapy units.</p>
      <p class="benefit">Deeply Moisturizes the<br>Skin and Restores<br>a Healthier<br>Look and Feel.</p>
    </div>

    <section class="label-info">
      <p class="ingredients-title">Ingredients:</p>
      <p class="ingredients-list">Paraffin waxes and Hydrocarbon waxes, Petrolatum,<br>Paraffin oils, Apricot kernel oil, Fragrance D &amp; C dyes.</p>
      <p class="caution-title">Caution:</p>
      <p class="caution-text">Paraffin is flammable. Do not use<br>near open flame or an unprotected resistance heater.</p>
      <p class="net-weight">Net Wt. 1 lb. (450 g.)</p>
    </section>
  </main>
</body>
</html>
```